Bref créative
Korvanta, LLC business cards & stationery -- letterhead, envelopes, proposals and invoices
Three-colors of the attached logo
Bright & Fun-filled
Milo Trenvik
President
3748 Pellow Lane
Fernbrook, MD 20937
milo@korvantallc.example
www.korvantallc.example
On the front of the card, I would like to see the tagline (Your complete IT department, when you need one.) separated from the logo and prominently positioned on the front of the card in such a way that it doesn't get lost with the logo and contact information. Thanks.
I'd like to see the following on the back in an artistic style consistent with the front of the card (I'm hoping it will all fit):
Korvanta is an affordable, skilled and experienced source for IT consulting and services. Our specialties include:
--Data and telecom network planning, engineering and construction
--PC and server hardware and software implementation and management
--Network (LAN/WAN) administration
--Remote and on-site Helpdesk assistance
--Communications and messaging systems
--Internet presence consultation and facilitation
--Backup and disaster recovery
--Voice over IP systems conversions
--Telecom account analysis
and much more! Call us today to find out how we can help you with your technology needs.
Korvanta, LLC logo file in AI format

```html
<!DOCTYPE html>
<html lang="en">
<head>
<meta charset="utf-8">
<title>Korvanta, LLC Stationery</title>
<link href="https://fonts.googleapis.com/css2?family=Montserrat:wght@700;800&family=Open+Sans:wght@400;600;700&display=swap" rel="stylesheet">
<style>
  :root {
    --bg: #e4e2de;
    --paper: #ffffff;
    --paper-shade: #f3f3f3;
    --green: #7dbb2c;
    --orange: #f08a24;
    --blue: #2f86c6;
    --ink: #4a4a4a;
    --ink-soft: #8a8a8a;
    --rule: #d5d5d5;
  }
  * { box-sizing: border-box; margin: 0; padding: 0; }
  html, body { width: 1200px; height: 696px; overflow: hidden; }
  body {
    background: var(--bg);
    font-family: "Open Sans", Arial, sans-serif;
    color: var(--ink);
    position: relative;
  }
  .piece {
    position: absolute;
    background: var(--paper);
    box-shadow: 0 2px 6px rgba(0,0,0,.18);
    overflow: hidden;
  }
  .brand {
    display: flex; align-items: center; gap: 3px;
    font-family: "Montserrat", Arial, sans-serif;
    font-weight: 800; color: var(--green); letter-spacing: .5px; line-height: 1;
  }
  .brand-square { background: var(--orange); display: inline-block; }
  .tagline { color: var(--blue); font-weight: 600; }

  /* business cards */
  .card { width: 168px; height: 96px; }
  .card-front .brand { position: absolute; left: 10px; top: 14px; font-size: 15px; }
  .card-front .brand-square { width: 9px; height: 9px; }
  .card-front .tagline { position: absolute; left: 10px; top: 33px; font-size: 5px; }
  .card-contact { position: absolute; right: 10px; top: 46px; font-size: 4.4px; line-height: 1.45; text-align: right; }
  .card-contact .name { font-weight: 700; font-size: 5.4px; color: var(--ink); }
  .card-contact .role { color: var(--orange); margin-bottom: 2px; }
  .card-band { position: absolute; left: 0; right: 0; bottom: 0; height: 5px; display: flex; }
  .card-band span { flex: 1; }
  .band-green { background: var(--green); }
  .band-orange { background: var(--orange); }
  .band-blue { background: var(--blue); }
  .card-back { padding: 8px 10px; font-size: 3.5px; line-height: 1.35; }
  .card-back .intro { font-weight: 600; color: var(--blue); margin-bottom: 2px; }
  .card-back ul { list-style: none; }
  .card-back li::before { content: "\25A0"; color: var(--green); margin-right: 2px; }
  .card-back .close { margin-top: 2px; color: var(--orange); font-weight: 600; }

  /* envelopes */
  .envelope { width: 264px; height: 96px; }
  .envelope .brand { position: absolute; left: 10px; top: 10px; font-size: 14px; }
  .envelope .brand-square { width: 8px; height: 8px; }
  .env-return { position: absolute; left: 10px; top: 28px; font-size: 4.4px; line-height: 1.4; }
  .env-stripe { position: absolute; left: 0; right: 0; bottom: 0; height: 4px; background: var(--blue); }
  .env-back svg { position: absolute; inset: 0; }

  /* letterhead */
  .letterhead { width: 216px; height: 446px; padding: 16px 20px 0 16px; }
  .letterhead .brand { font-size: 16px; }
  .letterhead .brand-square { width: 10px; height: 10px; }
  .letterhead .tagline { font-size: 4.6px; margin: 2px 0 16px; }
  .edge-stripe { position: absolute; top: 0; right: 0; width: 6px; height: 100%; background: var(--orange); }
  .letter-body { font-size: 4.2px; line-height: 1.6; color: var(--ink-soft); }
  .letter-body p { margin-bottom: 6px; }
  .sheet-footer {
    position: absolute; left: 0; right: 0; bottom: 0; height: 20px;
    border-top: 2px solid var(--blue);
    display: flex; justify-content: space-between; align-items: center;
    padding: 0 14px 0 16px; font-size: 3.8px; color: var(--ink-soft);
  }

  /* invoice */
  .invoice { width: 216px; height: 446px; padding: 16px 16px 0 16px; }
  .invoice .brand { font-size: 16px; }
  .invoice .brand-square { width: 10px; height: 10px; }
  .invoice .tagline { font-size: 4.6px; margin: 2px 0 12px; }
  .invoice-head { display: flex; justify-content: space-between; margin-bottom: 10px; }
  .invoice-title { font-family: "Montserrat", Arial, sans-serif; font-weight: 700; color: var(--orange); font-size: 9px; }
  .invoice-meta { font-size: 4px; line-height: 2; color: var(--ink-soft); width: 70px; }
  .invoice-meta div { border-bottom: 1px solid var(--rule); }
  .bill-to { font-size: 4px; color: var(--ink-soft); border-bottom: 1px solid var(--rule); width: 90px; margin-bottom: 12px; line-height: 2; }
  .invoice-table { width: 100%; border-collapse: collapse; font-size: 4px; }
  .invoice-table th { background: var(--blue); color: #fff; font-weight: 600; padding: 2px 3px; text-align: left; }
  .invoice-table td { height: 9px; border-bottom: 1px solid var(--rule); border-right: 1px solid var(--rule); }
  .invoice-table td:last-child { border-right: 0; }
  .invoice-table tr:nth-child(even) td { background: var(--paper-shade); }
  .invoice-totals { display: flex; justify-content: space-between; align-items: flex-end; margin-top: 8px; font-size: 4px; }
  .invoice-totals .thanks { color: var(--green); font-weight: 600; font-size: 5px; }
  .invoice-totals .sums div { width: 60px; border-bottom: 1px solid var(--rule); line-height: 2; }
</style>
</head>
<body>

  <!-- business card front -->
  <div class="piece card card-front" style="left:228px; top:84px;">
    <div class="brand"><span class="brand-square"></span>KORVANTA</div>
    <div class="tagline">Your complete IT department, when you need one.</div>
    <div class="card-contact">
      <div class="name">Milo Trenvik</div>
      <div class="role">President</div>
      <div>3748 Pellow Lane</div>
      <div>Fernbrook, MD 20937</div>
      <div>(410) 555-0182</div>
      <div>milo@korvantallc.example</div>
      <div>www.korvantallc.example</div>
    </div>
    <div class="card-band"><span class="band-green"></span><span class="band-orange"></span><span class="band-blue"></span></div>
  </div>

  <!-- business card front, second -->
  <div class="piece card card-front" style="left:228px; top:174px;">
    <div class="brand"><span class="brand-square"></span>KORVANTA</div>
    <div class="tagline">Your complete IT department, when you need one.</div>
    <div class="card-contact">
      <div class="name">Milo Trenvik</div>
      <div class="role">President</div>
      <div>3748 Pellow Lane</div>
      <div>Fernbrook, MD 20937</div>
      <div>(410) 555-0182</div>
      <div>milo@korvantallc.example</div>
      <div>www.korvantallc.example</div>
    </div>
    <div class="card-band"><span class="band-green"></span><span class="band-orange"></span><span class="band-blue"></span></div>
  </div>

  <!-- business card back -->
  <div class="piece card card-back" style="left:402px; top:174px;">
    <div class="intro">Korvanta is an affordable, skilled and experienced source for IT consulting and services. Our specialties include:</div>
    <ul>
      <li>Data and telecom network planning, engineering and construction</li>
      <li>PC and server hardware and software implementation and management</li>
      <li>Network (LAN/WAN) administration</li>
      <li>Remote and on-site Helpdesk assistance</li>
      <li>Communications and messaging systems</li>
      <li>Internet presence consultation and facilitation</li>
      <li>Backup and disaster recovery</li>
      <li>Voice over IP systems conversions</li>
      <li>Telecom account analysis</li>
    </ul>
    <div class="close">and much more! Call us today to find out how we can help you with your technology needs.</div>
    <div class="card-band"><span class="band-green"></span><span class="band-orange"></span><span class="band-blue"></span></div>
  </div>

  <!-- envelope back -->
  <div class="piece envelope env-back" style="left:216px; top:250px;">
    <svg width="264" height="96" viewBox="0 0 264 96" aria-hidden="true">
      <polyline points="0,0 132,52 264,0" fill="none" stroke="#d9d9d9" stroke-width="1"/>
      <line x1="0" y1="96" x2="110" y2="44" stroke="#e6e6e6" stroke-width="1"/>
      <line x1="264" y1="96" x2="154" y2="44" stroke="#e6e6e6" stroke-width="1"/>
    </svg>
  </div>

  <!-- envelope front -->
  <div class="piece envelope" style="left:216px; top:358px;">
    <div class="brand"><span class="brand-square"></span>KORVANTA</div>
    <div class="env-return">3748 Pellow Lane<br>Fernbrook, MD 20937</div>
    <div class="env-stripe"></div>
  </div>

  <!-- letterhead -->
  <div class="piece letterhead" style="left:480px; top:84px;">
    <div class="brand"><span class="brand-square"></span>KORVANTA</div>
    <div class="tagline">Your complete IT department, when you need one.</div>
    <div class="letter-body">
      <p>Dear Client,</p>
      <p>Thank you for considering Korvanta for your technology needs. Our team plans, builds and supports networks, servers and desktops for growing offices across the region, and we treat every client system as if it were our own.</p>
      <p>We offer remote and on-site helpdesk help, backup and disaster recovery, voice over IP changes and careful account reviews. Each project begins with a plain plan, a fair quote and a clear schedule you can count on.</p>
      <p>Please call us today to learn how we can help your business run smoothly.</p>
      <p>Sincerely,</p>
      <p style="color:var(--ink); font-weight:600;">Milo Trenvik</p>
    </div>
    <div class="edge-stripe"></div>
    <div class="sheet-footer">
      <span>3748 Pellow Lane<br>Fernbrook, MD 20937</span>
      <span>P (410) 555-0182<br>F (410) 555-0197</span>
      <span>www.korvantallc.example</span>
    </div>
  </div>

  <!-- invoice -->
  <div class="piece invoice" style="left:720px; top:84px;">
    <div class="brand"><span class="brand-square"></span>KORVANTA</div>
    <div class="tagline">Your complete IT department, when you need one.</div>
    <div class="invoice-head">
      <div class="invoice-title">INVOICE</div>
      <div class="invoice-meta"><div>Invoice No.</div><div>Date</div></div>
    </div>
    <div class="bill-to">Bill To</div>
    <table class="invoice-table">
      <thead><tr><th style="width:60%">Description</th><th>Qty</th><th>Amount</th></tr></thead>
      <tbody>
        <tr><td></td><td></td><td></td></tr><tr><td></td><td></td><td></td></tr>
        <tr><td></td><td></td><td></td></tr><tr><td></td><td></td><td></td></tr>
        <tr><td></td><td></td><td></td></tr><tr><td></td><td></td><td></td></tr>
        <tr><td></td><td></td><td></td></tr><tr><td></td><td></td><td></td></tr>
        <tr><td></td><td></td><td></td></tr><tr><td></td><td></td><td></td></tr>
        <tr><td></td><td></td><td></td></tr><tr><td></td><td></td><td></td></tr>
        <tr><td></td><td></td><td></td></tr><tr><td></td><td></td><td></td></tr>
        <tr><td></td><td></td><td></td></tr><tr><td></td><td></td><td></td></tr>
        <tr><td></td><td></td><td></td></tr><tr><td></td><td></td><td></td></tr>
      </tbody>
    </table>
    <div class="invoice-totals">
      <div class="thanks">Thank you for your business!</div>
      <div class="sums"><div>Subtotal</div><div>Total</div></div>
    </div>
    <div class="edge-stripe" style="background:var(--green)"></div>
    <div class="sheet-footer">
      <span>3748 Pellow Lane<br>Fernbrook, MD 20937</span>
      <span>P (410) 555-0182<br>F (410) 555-0197</span>
      <span>www.korvantallc.example</span>
    </div>
  </div>

  <!-- small envelope -->
  <div class="piece envelope" style="left:480px; top:548px; width:156px; height:88px;">
    <div class="brand" style="font-size:12px;"><span class="brand-square" style="width:7px;height:7px;"></span>KORVANTA</div>
    <div class="env-return" style="top:26px;">3748 Pellow Lane, Fernbrook, MD 20937</div>
  </div>

</body>
</html>
```